Personal coach needs brochure design for inspirational essay about authenticity

Overview:
I want a beautiful brochure, 11”x17” that folds to 8-1/2”x11” with 4 pages. Think of it as an oversize greeting card.
• Front cover: photograph of a dancer and title with attribution of quote (Lumafold jpeg photo attached)
• Inside spread: Copy (Helena Brisk copy attached) with some appropriate illustration, based on cover photo
• Back cover: contact information, brief descriptive copy, two small photos (jpeg photo attached; see copy for direction)
Copy for front cover title, inside spread and back cover is attached in doc titled "Helena Brisk copy"

Purpose of brochure:
I'm a personal coach and once a year I produce a 4-page illustrated inspirational essay, which invites personal reflection on living a more mindful, meaningful life. Most people I send them to collect them. Someday in the future I'd like to put a collection of these essays into a coffee table book and also create a website for the collection, which is related to the personal coaching that I do.
I have the brochures printed hard copy. I have attached a few examples from previous years. Each has a unique design related to its theme.

Concept:
This year’s essay theme, “There will only ever be one you!” is based on a quote by Helena Brisk, a famous modern dancer. The complete quote, which appears in the copy, is about being true to one’s authentic self. The essay is not about dance, but because the author of the quote was a dancer who personified this theme of being unique to self, I have selected a photo of dance for the cover.

Design Guidance:
Front cover: One possibility is to expand the background color of the Lumafold photo so the photo seems to emerge from the background. But I am open to ideas. I think the photo is artsy enough as it is, but there may be other ways to treat it (e.g. special effects) that would also work. The title should appear somewhere. Make the attribution (--Helena Brisk) in smaller type than the title.

Inside Spread: There may be ways to borrow a design motif from the cover photo to make the inside spread more visually interesting, i.e., not just straight copy. I think it may be helpful to make the font size of the quote larger than the rest of the copy, but it has to be read in sequence. Or maybe it's printed in same size as copy, but then also repeated and displayed by itself in larger type.

Back cover: If you look at some of the other examples I’ve sent, you’ll see how the back cover is typically handled. I want a reduced version of the cover to be placed near the line that says "this is the 16th in a series.." Then, there’s a jpeg photo of Helena Brisk that should be placed next to the copy description of her.

Need extra days to review

```html
<!DOCTYPE html>
<html lang="en">
<head>
<meta charset="utf-8">
<title>There Will Only Ever Be One You – Inside Spread</title>
<link rel="stylesheet" href="https://fonts.googleapis.com/css2?family=Poiret+One&family=Questrial&display=swap">
<style>
  :root {
    --paper: #ffffff;
    --ink: #151515;
    --heading-blue: #5a7eae;
    --ornament-light: rgba(169, 191, 220, 0.55);
    --ornament-dark: rgba(107, 141, 186, 0.7);
  }
  html, body {
    margin: 0;
    padding: 0;
    width: 926px;
    height: 1200px;
    overflow: hidden;
    background: var(--paper);
  }
  .essay-page {
    position: relative;
    width: 926px;
    height: 1200px;
    overflow: hidden;
    background: var(--paper);
  }
  .essay-section {
    position: absolute;
    left: 60px;
    width: 866px;
  }
  .section-ornament {
    position: absolute;
    left: 0;
    top: -3px;
    width: 21px;
    height: 74px;
    border-radius: 11px;
    background:
      radial-gradient(ellipse at 50% 50%, var(--ornament-dark) 0%, var(--ornament-light) 45%, rgba(255,255,255,0) 75%);
  }
  .section-heading {
    margin: 0 0 0 34px;
    height: 72px;
    font-family: "Poiret One", "Century Gothic", sans-serif;
    font-weight: 400;
    font-size: 38px;
    line-height: 36px;
    letter-spacing: -0.2px;
    text-transform: uppercase;
    color: var(--heading-blue);
  }
  .section-body {
    margin: 2px 0 0 34px;
    font-family: "Questrial", "Century Gothic", sans-serif;
    font-size: 19.4px;
    line-height: 24.3px;
    white-space: nowrap;
    color: var(--ink);
  }
  .section-village     { top: 75px; }
  .section-surprise    { top: 299px; }
  .section-irreverence { top: 495px; }
  .section-impulse     { top: 720px; }
  .section-compelled   { top: 946px; }
  .section-impulse .section-body { margin-top: 8px; }
</style>
</head>
<body>
<main class="essay-page">

  <section class="essay-section section-village">
    <div class="section-ornament" role="img" aria-label="Small blue floral vine ornament"></div>
    <h2 class="section-heading">In the rural<br>Ohio village</h2>
    <p class="section-body">where I grew up, one of the highlights of Sunday morning church service -- in between<br>congregational hymn-singing and the preacher’s sermon -- was the “special selection,” a<br>musical performance by a parishioner. Typically, it was a vocalist or instrumental on piano,<br>organ or violin.</p>
  </section>

  <section class="essay-section section-surprise">
    <div class="section-ornament" role="img" aria-label="Small blue floral vine ornament"></div>
    <h2 class="section-heading">One Sunday, we<br>were surprised</h2>
    <p class="section-body">by an unusual performance.&nbsp; A plump, buxom farm wife approached the pulpit,<br>puckered up her lips and unexpectedly began to whistle the hymn “The Old Rugged<br>Cross.” As a 10-year-old, I found this hilarious as I tried to choke back my wide-eyed</p>
  </section>

  <section class="essay-section section-irreverence">
    <div class="section-ornament" role="img" aria-label="Small blue floral vine ornament"></div>
    <h2 class="section-heading">Despite the<br>irreverence</h2>
    <p class="section-body">of my pre-adolescent reaction, this memory has stayed with me for decades as an iconic<br>example of the wonderment of individual differences. Of the delight I find in witnessing<br>someone express herself in sometimes surprising and even courageous ways. Of the<br>marvel of beholding a person be truly authentic and uniquely original.</p>
  </section>

  <section class="essay-section section-impulse">
    <div class="section-ornament" role="img" aria-label="Small blue floral vine ornament"></div>
    <h2 class="section-heading">Someone who personified<br>the irrepressible impulse</h2>
    <p class="section-body">to express her individuality was the early 20th century dancer and choreographer Helena<br>Brisk.&nbsp; A pioneer of modern dance, she&nbsp; threw tradition overboard and was inspired<br>to dance in a way that was a radical departure from the formalized style and rigidly<br>dictated forms of classical ballet.</p>
  </section>

  <section class="essay-section section-compelled">
    <div class="section-ornament" role="img" aria-label="Small blue floral vine ornament"></div>
    <h2 class="section-heading">Brisk felt<br>compelled to</h2>
    <p class="section-body">express the rawness and emotion of human experience in her dancing -- not just present<br>a form of pretty entertainment. Iconoclastically brilliant, she created a new language of<br>dance, a revolutionary vocabulary of movement that electrified the stage, often creating<br>a visceral response in the audience.</p>
  </section>

</main>
</body>
</html>
```